Flask Up Fable needs wedding label designs!

Flask Up Fable is looking for new wedding designs! Please look at http://www.flaskupfable.com/water-bottle-labels and http://www.flaskupfable.com/custom-water to get an idea of what we currently offer.

These new designs will be saved onto Flask Up Fable so that customers can come and customize the text and/or add pictures on them for purchase as water bottle labels or custom label bottled water.

Designs must appeal to a broad audience so any and all styles will be considered. Some other sites to draw inspiration from are plumquill.com, velcrest.com, vowsheetmuses.com and ferlow.com.

Questions? Ask away!

Target Market(s)

Target market is brides, mothers of brides and wedding planners.

Industry/Entity Type

Wedding

Requirements
Must have
• Designs must be at 300 dpi in CMYK. Width is 8.133" Height is 2.377" with a .125" bleed around all sides.

```html
<!DOCTYPE html>
<html lang="en">
<head>
<meta charset="utf-8">
<title>Benjamin and Mary – Wedding Water Bottle Label</title>
<link rel="stylesheet" href="https://fonts.googleapis.com/css2?family=Great+Vibes&family=Delius&display=swap">
<style>
  :root {
    --frame: #fbf1e8;
    --frame-edge: #f1dfcc;
    --paper: #fbf0ee;
    --paper-light: #fdf6f4;
    --title-pink: #f2a9c2;
    --thanks-brown: #7a3710;
    --art-blue: #7cc6ef;
    --art-pink: #f7bcd0;
    --art-branch: #a0522d;
  }
  html, body {
    margin: 0;
    padding: 0;
    overflow: hidden;
    background: #ffffff;
  }
  .label {
    position: relative;
    width: 1200px;
    height: 352px;
    box-sizing: border-box;
    background: var(--frame);
    border: 2px solid var(--frame-edge);
    overflow: hidden;
  }
  .label__panel {
    position: absolute;
    left: 16px;
    top: 16px;
    right: 16px;
    bottom: 16px;
    background: radial-gradient(ellipse at center, var(--paper-light) 0%, var(--paper) 100%);
  }
  .label__names {
    position: absolute;
    left: 0;
    right: 0;
    top: 44px;
    margin: 0;
    text-align: center;
    font-family: "Great Vibes", cursive;
    font-weight: 400;
    font-size: 64px;
    line-height: 1;
    color: var(--title-pink);
  }
  .label__lovebirds {
    position: absolute;
    left: 446px;
    top: 124px;
    width: 268px;
    height: 122px;
  }
  .label__thanks {
    position: absolute;
    left: 0;
    right: 0;
    top: 252px;
    margin: 0;
    text-align: center;
    font-family: "Delius", cursive;
    font-size: 33px;
    letter-spacing: 1.5px;
    line-height: 1.2;
    color: var(--thanks-brown);
  }
</style>
</head>
<body>
  <div class="label">
    <div class="label__panel"></div>
    <h1 class="label__names">Benjamin and Mary</h1>
    <svg class="label__lovebirds" viewBox="0 0 268 122" role="img" aria-label="Illustration of a blue bird and a pink bird perched together on a blossoming brown branch">
      <defs>
        <linearGradient id="lovebirds-tone" x1="0" y1="0" x2="1" y2="0">
          <stop offset="0" stop-color="var(--art-blue)" stop-opacity="0.55"/>
          <stop offset="0.5" stop-color="var(--art-branch)" stop-opacity="0.25"/>
          <stop offset="1" stop-color="var(--art-pink)" stop-opacity="0.7"/>
        </linearGradient>
      </defs>
      <rect x="0" y="0" width="268" height="122" rx="40" fill="url(#lovebirds-tone)"/>
    </svg>
    <p class="label__thanks">Thank you for being here to celebrate with us!</p>
  </div>
</body>
</html>
```